WP website design (TOVI)

We need a wordpress design that will incorporate a professional color scheme with company logo in a clean layout. The design needs to consider that this will be developed on a responsive theme. Colors are undetermined - those that will complement the logo.
Client mentions liking plinmerbid.com for the layout and use of color. Possible but not necessary to have large slideshow element.

Industry/Entity Type

It Company

Font styles to use
Sans Serif

Colors

Designer to choose colors to be used in the design.

Requirements
Must have
• - Navigation: 1)Home 2) Auctions 3) Services 4) About Us 5) FAQs 6) References 7) Contact Us

Site will have slideshow, please use high-end stock real estate image initially. Header will have logo. Social icons (Facebook, Twitter, Youtube)

Widgets Include: Email signup form, Featured Auctions, Featured Video widget.

Footer will have contact info (below), site navigation, smaller company logo, affiliation logos (attached).

TOVI Auction Group
4275 Birch Vale Lane
Marlowe, KY 40617
1-800-419-BIDS (2437)
Ph. (270) 386-9041
Fx. (270) 386-1158
Nice to have
• - Site will have drop-down menus - please indicate the styling, for instance the dropdown menus 1) Live 2) Online 3) Past - under the 'Auctions' link

```html
<!DOCTYPE html>
<html lang="en">
<head>
<meta charset="utf-8">
<title>TOVI Auction Group</title>
<link rel="stylesheet" href="https://fonts.googleapis.com/css2?family=Carlito:wght@400;700&family=Arimo:ital,wght@0,400;0,700;1,400;1,700&family=Tinos&display=swap">
<style>
:root{
  --brown:#5b3112;
  --brown-mid:#7b4511;
  --red:#c8141c;
  --red-band:rgba(200,16,24,.88);
  --dark:#393939;
  --ink:#222;
  --white:#fff;
  --grey:#777;
}
*{box-sizing:border-box;margin:0;padding:0}
html,body{width:857px;height:1200px;overflow:hidden;background:var(--white)}
body{position:relative;font-family:"Carlito",sans-serif;color:var(--ink)}
.abs{position:absolute}

.brand{left:72px;top:30px;font-weight:700;font-size:24px;color:var(--red);line-height:1}
.brand small{display:block;font-size:13px;margin-top:2px}
.follow{left:601px;top:50px;font-family:"Arimo",sans-serif;font-size:15px;color:#444}
.social{left:690px;top:46px;display:flex;gap:8px}
.social span{width:26px;height:26px;border-radius:50%}

.nav{left:0;top:98px;width:857px;height:32px;background:var(--brown)}
.nav a{position:absolute;top:0;line-height:32px;color:var(--white);font-size:12px;text-decoration:none;transform:translateX(-50%)}
.nav .sep{position:absolute;top:0;width:1px;height:32px;background:#3e200a}
.nav .active{top:7px;line-height:18px;background:var(--red);padding:0 6px;border-radius:3px}
.nav .active::after{content:"";position:absolute;left:50%;bottom:-4px;margin-left:-4px;border:4px solid transparent;border-bottom:0;border-top-color:var(--red)}

.dropdown{left:110px;top:133px;width:146px;height:103px;background:rgba(255,255,255,.9);border:1px solid #ddd;z-index:3}
.dropdown a{position:absolute;left:6px;width:132px;height:20px;border-radius:2px;background:#3b3b3b;color:var(--white);font-family:"Arimo",sans-serif;font-size:8px;line-height:20px;padding-left:18px;text-decoration:none}
.dropdown a::before{content:"";position:absolute;left:9px;top:7px;border:3px solid transparent;border-right:0;border-left-color:var(--white)}
.dropdown a.on{background:var(--brown-mid)}

.hero{left:0;top:130px;width:857px;height:330px;background:linear-gradient(180deg,#b9cde0 0%,#d9e2ea 30%,#8f7d5e 55%,#76694c 80%,#5f7a33 100%)}
.hero-band{left:0;top:419px;width:857px;height:41px;background:var(--red-band);text-align:center;color:var(--white);font-family:"Arimo",sans-serif;font-size:12.5px;padding-top:9px}
.dots{left:407px;top:447px;display:flex;gap:7px}
.dots span{width:7px;height:7px;border-radius:50%;background:var(--white)}
.dots span:first-child{background:#333}

.featured-title{left:70px;top:504px;font-size:19px;color:var(--red);letter-spacing:.5px}
.featured-sub{left:71px;top:538px;font-family:"Tinos",serif;font-size:12px;letter-spacing:.3px}
.thumb{left:73px;top:566px;width:137px;height:61px;background:linear-gradient(180deg,#bcd3ea,#c9b595 55%,#6f8a3c)}
.btn{top:634px;height:22px;color:var(--white);font-family:"Arimo",sans-serif;font-weight:700;font-size:9.5px;line-height:20px;padding-left:22px;border:1px solid #999}
.btn::before{content:"";position:absolute;left:8px;top:6px;width:9px;height:8px;border-radius:50%;background:var(--white)}
.btn-details{left:72px;width:66px;background:#262626}
.btn-gallery{left:147px;width:65px;background:var(--red)}
.btn-gallery::before{border-radius:1px}
.auction-info{left:226px;top:566px;width:290px;font-family:"Arimo",sans-serif;font-size:8.3px;line-height:14.4px;font-style:italic}
.auction-info h3{font-style:normal;font-size:10px;color:var(--brown-mid);margin-bottom:1px}
.auction-info b{color:var(--red)}
.auction-info p+p{margin-top:4px}

.signup{left:576px;top:499px;width:210px;height:177px;background:var(--brown-mid);border-radius:3px;color:var(--white);padding:8px 14px}
.signup h2{font-weight:400;font-size:20px;letter-spacing:.5px}
.signup p{font-family:"Arimo",sans-serif;font-size:8.2px;line-height:11px;margin-top:2px;text-align:justify}
.field{position:absolute;left:16px;width:175px;height:21px;background:var(--white);border:1px solid #bbb;font-family:"Arimo",sans-serif;font-size:9px;color:#888;line-height:19px;padding-left:6px}
.subscribe{position:absolute;left:16px;top:139px;width:73px;height:21px;background:#2b2b2b;border-radius:3px;text-align:center;line-height:21px;font-size:11px;letter-spacing:.5px}

.video-title{left:0;top:722px;width:857px;text-align:center;font-size:23px;letter-spacing:.5px}
.video-band{left:0;top:766px;width:857px;height:300px;background:linear-gradient(180deg,#d6d6d6,#9a9a9a 65%,#5b5b5b)}
.video-frame{left:114px;top:780px;width:625px;height:262px;background:#2a2a2a;padding:4px}
.video-frame .media{width:100%;height:100%;background:linear-gradient(180deg,#4d6fb5,#7b87c0 45%,#44455a 75%,#3a3226)}
.video-frame svg{position:absolute;left:276px;top:98px}

.footer{left:0;top:1066px;width:857px;height:110px;background:var(--dark);color:var(--white)}
.address{left:76px;top:18px;font-size:10.3px;line-height:14.5px;letter-spacing:.3px}
.foot-nav a{position:absolute;top:25px;color:var(--white);font-size:9.5px;text-decoration:none}
.foot-brand{left:460px;top:58px;font-weight:700;font-size:12px;line-height:1.05;width:70px;text-align:center}
.badge{top:52px;height:46px;background:#e8e8e8}
.copyright{left:0;top:1176px;width:857px;height:24px;background:var(--red);color:var(--white);text-align:center;font-family:"Arimo",sans-serif;font-size:8.3px;line-height:24px}
</style>
</head>
<body>

<header>
  <div class="abs brand">TOVI<small>Auction Group</small></div>
  <div class="abs follow">Follow Us:</div>
  <div class="abs social">
    <span style="background:#3b5998" aria-label="Social link"></span>
    <span style="background:#29a9e0" aria-label="Social link"></span>
    <span style="background:#d43a2c" aria-label="Social link"></span>
  </div>
</header>

<nav class="abs nav">
  <a style="left:102px">Home</a>
  <span class="sep" style="left:136px"></span>
  <a class="active" style="left:182px">Auctions</a>
  <span class="sep" style="left:223px"></span>
  <a style="left:265px">Services</a>
  <span class="sep" style="left:307px"></span>
  <a style="left:350px">About Us</a>
  <span class="sep" style="left:395px"></span>
  <a style="left:428px">FAQs</a>
  <span class="sep" style="left:461px"></span>
  <a style="left:510px">References</a>
  <span class="sep" style="left:557px"></span>
  <a style="left:605px">Contact Us</a>
</nav>

<div class="abs dropdown">
  <a class="on" style="top:15px">Live</a>
  <a style="top:43px">Online</a>
  <a style="top:71px">Past</a>
</div>

<div class="abs hero" role="img" aria-label="Slideshow photo of a large craftsman-style suburban house under a blue sky"></div>
<div class="abs hero-band">LOREM IPSUM DOLOR SIT AMET, CONSECTETUR</div>
<div class="abs dots"><span></span><span></span><span></span><span></span></div>

<section>
  <h2 class="abs featured-title" style="font-weight:400">Featured Auctions</h2>
  <div class="abs featured-sub">SHOP EQUIPMENT/TOOLS * PORK PROCESSING ITEMS</div>
  <div class="abs thumb" role="img" aria-label="Photo of the auction property, a two-storey house"></div>
  <div class="abs btn btn-details">Details</div>
  <div class="abs btn btn-gallery">Gallery</div>
  <div class="abs auction-info">
    <h3>LIVE ON-SITE AUCTION</h3>
    <p><b>Begins:</b>&nbsp; Tuesday, April 23, 2013 at 10:00 AM EDT</p>
    <p><b>Location:</b>&nbsp; Cedar Ridge Entrance- 1450 N. Valley Rd 18&nbsp; text of the printing and typesetting industry. Lorem Ipsum&nbsp; text of the printing and typesettinghas been&nbsp; text of the printing and typesetting the industry's standard dummy text ever since the 1500s,</p>
  </div>
</section>

<aside class="abs signup">
  <h2>Email Sign Up</h2>
  <p>Lorem ipsum dolor sit amet, consectetuer adipiscing elit. Nam</p>
  <div class="field" style="top:73px">Your Name</div>
  <div class="field" style="top:109px">Email Address</div>
  <div class="subscribe">Subscribe</div>
</aside>

<h2 class="abs video-title" style="font-weight:400">Feature Video</h2>
<div class="abs video-band" role="img" aria-label="Greyscale city skyline backdrop"></div>
<div class="abs video-frame">
  <div class="media" role="img" aria-label="Video still of a modern house at dusk"></div>
  <svg width="72" height="72" viewBox="0 0 72 72">
    <circle cx="36" cy="36" r="32" fill="rgba(0,0,0,.15)" stroke="rgba(255,255,255,.6)" stroke-width="5"/>
    <path d="M27 20 L53 36 L27 52 Z" fill="rgba(255,255,255,.6)"/>
  </svg>
</div>

<footer class="abs footer">
  <div class="abs address">TOVI Auction Group<br>4275 Birch Vale Lane<br>Marlowe, KY 40617<br>1-800-419-BIDS (2437)<br>Ph. (270) 386-9041<br>Fx. (270) 386-1158</div>
  <div class="foot-nav">
    <a style="left:328px">Home</a>
    <a style="left:387px">Auctions</a>
    <a style="left:458px">Services</a>
    <a style="left:526px">About Us</a>
    <a style="left:598px">FAQs</a>
    <a style="left:653px">References</a>
    <a style="left:732px">Contact Us</a>
  </div>
  <div class="abs foot-brand">TOVI Auction Group</div>
  <div class="abs badge" style="left:545px;width:36px" aria-label="Affiliation badge"></div>
  <div class="abs badge" style="left:592px;width:74px;top:60px;height:32px;border-radius:50%" aria-label="Affiliation badge"></div>
  <div class="abs badge" style="left:677px;width:43px" aria-label="Affiliation badge"></div>
  <div class="abs badge" style="left:731px;width:43px" aria-label="Affiliation badge"></div>
</footer>
<div class="abs copyright">Copyright (C) Tovi auction group. 2013.&nbsp; All Rights Reserved</div>

</body>
</html>
```